Business Card design for construction company

I would like a business card design for a construction company - Harlow Constructions. I have attached the ai logo file for use. I would like the card to be very smart and clean and incorporate only white and the two colours in the logo. I would like the card to have two sides. One side can just have the logo, the other with the relevant information.

Target Market(s)

Building and Construction Clients

Industry/Entity Type

Business

Contact Information for Business Card

Name: Tom Pardoe
Company: Harlow Constructions Pty Limited
Address: 14 Mallee Crescent Carrow Vale 2093
Phone: 0427 531 068
Email: tomp@harlowbuild-example.com.au

Font styles to use
Serif
Sans Serif

Requirements
Must have
• Details noted above
• Logo as provided
• Colours as in logo
• Square edges
• A font that compliments the logo
Should not have
• Any colour other than white and those in logo
• Rounded edges

```html
<!DOCTYPE html>
<html lang="en">
<head>
<meta charset="utf-8">
<title>Harlow Constructions – Tom Pardoe</title>
<link href="https://fonts.googleapis.com/css2?family=Jost:wght@300;400&display=swap" rel="stylesheet">
<style>
  :root {
    --slate: #58585a;
    --sky: #29a9e0;
    --white: #ffffff;
  }
  * { margin: 0; padding: 0; box-sizing: border-box; }
  html, body { width: 1200px; height: 734px; overflow: hidden; background: var(--slate); }
  .card {
    position: relative;
    width: 1200px;
    height: 734px;
    background: var(--slate);
    font-family: "Jost", "Futura", sans-serif;
    color: var(--white);
  }
  .brand {
    position: absolute;
    top: 143px;
    left: 0;
    width: 1200px;
    text-align: center;
    font-weight: 400;
    font-size: 50px;
    letter-spacing: 6px;
    text-transform: uppercase;
    line-height: 1;
  }
  .holder {
    position: absolute;
    top: 282px;
    left: 0;
    width: 1214px;
    text-align: center;
    font-weight: 400;
    font-size: 57px;
    line-height: 1;
  }
  .band {
    position: absolute;
    left: 0;
    width: 1200px;
    height: 13px;
    background: var(--sky);
  }
  .band--top { top: 381px; }
  .band--bottom { top: 684px; }
  .panel {
    position: absolute;
    top: 407px;
    height: 264px;
    background: var(--sky);
  }
  .panel--left { left: 0; width: 585px; }
  .panel--right { left: 614px; width: 586px; }
  .contact {
    position: absolute;
    display: flex;
    align-items: center;
    gap: 0;
  }
  .contact__icon {
    position: absolute;
    width: 60px;
    height: 60px;
  }
  .contact__text {
    position: absolute;
    font-weight: 300;
    white-space: nowrap;
    line-height: 1;
  }
  .phone-text { left: 165px; top: 470px; font-size: 35px; letter-spacing: 1px; }
  .web-text { left: 167px; top: 576px; font-size: 31px; }
  .email-text { left: 730px; top: 472px; font-size: 28.5px; }
  .address-text { left: 730px; top: 552px; font-size: 32px; line-height: 40px; }
</style>
</head>
<body>
<div class="card">
  <div class="brand">Harlow Constructions</div>
  <div class="holder">Tom Pardoe</div>

  <div class="band band--top"></div>
  <div class="panel panel--left"></div>
  <div class="panel panel--right"></div>
  <div class="band band--bottom"></div>

  <svg class="contact__icon" style="left:84px;top:459px" viewBox="0 0 60 60" aria-hidden="true">
    <circle cx="30" cy="30" r="30" fill="var(--slate)"/>
    <path d="M20 17c2-1 3-1 4 1l3 5c1 2 0 3-1 4l-1 1c1 3 4 6 7 7l1-1c1-1 2-2 4-1l5 3c2 1 2 2 1 4-2 3-5 4-9 2-6-3-11-8-14-14-2-4-1-8 0-11z" fill="var(--white)"/>
  </svg>
  <div class="contact__text phone-text">0427 531 068</div>

  <svg class="contact__icon" style="left:84px;top:561px" viewBox="0 0 60 60" aria-hidden="true">
    <circle cx="30" cy="30" r="30" fill="var(--slate)"/>
    <circle cx="30" cy="30" r="16" fill="none" stroke="var(--white)" stroke-width="3"/>
    <ellipse cx="30" cy="30" rx="7" ry="16" fill="none" stroke="var(--white)" stroke-width="2"/>
    <line x1="14" y1="30" x2="46" y2="30" stroke="var(--white)" stroke-width="2"/>
  </svg>
  <div class="contact__text web-text">www.harlowbuild-example.com</div>

  <svg class="contact__icon" style="left:649px;top:459px" viewBox="0 0 60 60" aria-hidden="true">
    <circle cx="30" cy="30" r="30" fill="var(--slate)"/>
    <rect x="14" y="19" width="32" height="22" fill="none" stroke="var(--white)" stroke-width="2.5"/>
    <polyline points="14,20 30,32 46,20" fill="none" stroke="var(--white)" stroke-width="2.5"/>
  </svg>
  <div class="contact__text email-text">tomp@harlowbuild-example.com.au</div>

  <svg class="contact__icon" style="left:649px;top:561px" viewBox="0 0 60 60" aria-hidden="true">
    <circle cx="30" cy="30" r="30" fill="var(--slate)"/>
    <path d="M30 48c-6-9-11-15-11-22a11 11 0 0 1 22 0c0 7-5 13-11 22z" fill="none" stroke="var(--white)" stroke-width="2.5"/>
    <circle cx="30" cy="26" r="4.5" fill="none" stroke="var(--white)" stroke-width="2.5"/>
  </svg>
  <div class="contact__text address-text">14 Mallee Crescent,<br>Carrow Vale 2093</div>
</div>
</body>
</html>
```